Linkmesa and Glimtoria advertising

We need Linkmesa and Glimtoria ads. Simple ad with Alaska themed background.
This ad is to introduce our new ZENIRO Internet service.
--Speeds to 500 mpbs
-- Packages start at only $89.99 for speeds to 100mbps
-- Fiber Optic based connection, Not satellite
-- Extreme low latency, consistent speeds
--FREE equipment, FREE Installation, FREE wifi router, First month of service FREE

```html
<!DOCTYPE html>
<html lang="en">
<head>
<meta charset="utf-8">
<title>Skyreach Broadband – ZENIRO Internet social ads</title>
<link rel="stylesheet" href="https://fonts.googleapis.com/css2?family=Prompt:wght@400;500;600;700&display=swap">
<style>
  :root {
    --board: #ffffff;
    --panel: rgba(26, 55, 125, 0.62);
    --url-bar: #0c5bab;
    --red: #e8192c;
    --white: #ffffff;
    --logo-ink: #1c2f5c;
    --caption: #2b2b2b;
    --sky: #f4f6f9;
    --mist: #c4d0df;
    --tundra: #6f86a6;
    --cliff: #4a6690;
    --water: #2a5ba6;
    --deep: #1a3f84;
  }
  * { box-sizing: border-box; margin: 0; padding: 0; }
  html, body { width: 1200px; height: 1011px; overflow: hidden; background: var(--board); }
  body { position: relative; font-family: "Prompt", sans-serif; color: var(--white); }

  .ad { position: absolute; overflow: hidden; box-shadow: 0 6px 14px rgba(0,0,0,0.35); }
  .ad--post { left: 38px; top: 184px; width: 610px; height: 610px; }
  .ad--story { left: 687px; top: 51px; width: 479px; height: 852px; }

  .ad__scenery { position: absolute; inset: 0; }
  .ad--post .ad__scenery {
    background:
      radial-gradient(ellipse 60% 22% at 70% 42%, rgba(210,222,236,0.45), transparent 70%),
      radial-gradient(ellipse 55% 18% at 20% 60%, rgba(120,140,160,0.45), transparent 70%),
      radial-gradient(ellipse 70% 30% at 55% 78%, rgba(70,120,190,0.5), transparent 70%),
      linear-gradient(180deg, var(--sky) 0%, var(--mist) 14%, #9fb1c9 24%, var(--tundra) 34%, var(--cliff) 48%, var(--water) 66%, #234f9c 84%, var(--deep) 100%);
  }
  .ad--story .ad__scenery {
    background:
      radial-gradient(ellipse 60% 14% at 70% 30%, rgba(210,222,236,0.45), transparent 70%),
      radial-gradient(ellipse 60% 14% at 25% 46%, rgba(120,140,160,0.4), transparent 70%),
      radial-gradient(ellipse 80% 18% at 55% 68%, rgba(70,120,190,0.5), transparent 70%),
      linear-gradient(180deg, var(--sky) 0%, var(--mist) 12%, #9fb1c9 20%, var(--tundra) 28%, var(--cliff) 40%, var(--water) 60%, #234f9c 80%, var(--deep) 100%);
  }

  .brand { position: absolute; display: flex; align-items: center; gap: 7px; font-weight: 600; color: var(--logo-ink); white-space: nowrap; letter-spacing: -0.3px; }
  .brand__dot { flex: none; border-radius: 50%; background: var(--red); }

  .headline { position: absolute; font-weight: 700; white-space: nowrap; text-shadow: 0 1px 3px rgba(20,40,90,0.35); }
  .headline__line { position: absolute; left: 0; display: block; }
  .headline__big { font-size: 1.75em; font-weight: 600; line-height: 0; }
  .headline__caps { font-weight: 500; font-size: 0.9em; }

  .panel { position: absolute; background: var(--panel); }
  .features { list-style: none; }
  .features li { position: absolute; line-height: 1.2; white-space: nowrap; }
  .features li::before { content: ""; position: absolute; border-radius: 50%; background: var(--red); }

  .free-tag { position: absolute; background: var(--red); font-weight: 700; text-align: center; }
  .perk { position: absolute; text-align: center; font-weight: 500; line-height: 1.15; }
  .perk svg { display: block; margin: 0 auto; }

  .url-bar { position: absolute; background: var(--url-bar); border-radius: 999px; text-align: center; white-space: nowrap; letter-spacing: 0.6px; }
  .url-bar strong { font-weight: 600; }
  .url-bar__dot { position: absolute; top: 50%; border-radius: 50%; background: var(--red); transform: translate(-50%, -50%); }

  .caption { position: absolute; color: var(--caption); font-size: 21px; font-weight: 500; white-space: nowrap; transform: translateX(-50%); }

  /* post sizes */
  .ad--post .brand { left: 54px; top: 68px; font-size: 26px; }
  .ad--post .brand__dot { width: 10px; height: 10px; }
  .ad--post .headline { left: 57px; top: 0; font-size: 33px; }
  .ad--post .headline__line { line-height: 38px; }
  .ad--post .headline__line--1 { top: 132px; }
  .ad--post .headline__line--2 { top: 170px; }
  .ad--post .panel--features { left: 44px; top: 235px; width: 395px; height: 262px; border-radius: 29px; }
  .ad--post .features li { left: 55px; font-size: 18.6px; }
  .ad--post .features li::before { left: -21px; top: 8px; width: 9px; height: 9px; }
  .ad--post .panel--perks { left: 468px; top: 236px; width: 107px; height: 262px; border-radius: 28px; overflow: hidden; }
  .ad--post .free-tag { left: 0; top: 0; width: 100%; height: 38px; font-size: 20px; line-height: 40px; border-radius: 28px 28px 0 0; }
  .ad--post .perk { left: 0; width: 100%; font-size: 9.5px; }
  .ad--post .url-bar { left: 34px; top: 545px; width: 542px; height: 42px; font-size: 18.6px; line-height: 42px; }
  .ad--post .url-bar__dot { width: 13px; height: 13px; }

  /* story sizes */
  .ad--story .brand { left: 76px; top: 124px; font-size: 21px; }
  .ad--story .brand__dot { width: 8px; height: 8px; }
  .ad--story .headline { left: 62px; top: 0; font-size: 24.5px; }
  .ad--story .headline__line { line-height: 29px; }
  .ad--story .headline__line--1 { top: 224px; }
  .ad--story .headline__line--2 { top: 253px; }
  .ad--story .panel--features { left: 61px; top: 312px; width: 358px; height: 238px; border-radius: 28px; }
  .ad--story .features li { left: 49px; font-size: 17.5px; }
  .ad--story .features li::before { left: -19px; top: 8px; width: 8px; height: 8px; }
  .ad--story .panel--perks { left: 61px; top: 606px; width: 358px; height: 95px; border-radius: 30px; }
  .ad--story .free-tag { left: 192px; top: 588px; width: 95px; height: 27px; font-size: 17px; line-height: 28px; border-radius: 14px; z-index: 2; }
  .ad--story .perk { width: 80px; top: 621px; font-size: 11.5px; transform: translateX(-50%); }
  .ad--story .url-bar { left: 41px; top: 766px; width: 389px; height: 30px; font-size: 12.8px; line-height: 30px; }
  .ad--story .url-bar__dot { width: 9px; height: 9px; }
</style>
</head>
<body>

<svg width="0" height="0" style="position:absolute" aria-hidden="true">
  <defs>
    <symbol id="icon-equipment" viewBox="0 0 32 32">
      <g fill="none" stroke="#fff" stroke-width="1.6" stroke-linecap="round">
        <path d="M10 8a9 9 0 0 1 12 0M12.5 10.5a5.5 5.5 0 0 1 7 0"/>
        <circle cx="16" cy="13" r="0.8" fill="#fff"/>
        <rect x="4" y="16" width="24" height="6" rx="1.5"/>
        <path d="M8 19h2M12 19h2M16 19h2M20 19h2M16 22v4M11 27h10"/>
      </g>
    </symbol>
    <symbol id="icon-install" viewBox="0 0 32 32">
      <g fill="none" stroke="#fff" stroke-width="1.6" stroke-linecap="round">
        <rect x="4" y="4" width="18" height="6" rx="1.5"/>
        <rect x="4" y="12" width="14" height="6" rx="1.5"/>
        <rect x="4" y="20" width="12" height="6" rx="1.5"/>
        <path d="M7 7h2M7 15h2M7 23h2"/>
        <circle cx="23" cy="22" r="6"/>
        <path d="M23 18.5v6M20.5 22l2.5 2.5 2.5-2.5"/>
      </g>
    </symbol>
    <symbol id="icon-router" viewBox="0 0 32 32">
      <g fill="none" stroke="#fff" stroke-width="1.6" stroke-linecap="round">
        <path d="M10 8a9 9 0 0 1 12 0M12.5 11a5 5 0 0 1 7 0"/>
        <circle cx="16" cy="14" r="0.8" fill="#fff"/>
        <rect x="4" y="18" width="24" height="8" rx="4"/>
        <path d="M13 22h1M16 22h1M19 22h1"/>
      </g>
    </symbol>
    <symbol id="icon-calendar" viewBox="0 0 32 32">
      <g fill="none" stroke="#fff" stroke-width="1.6" stroke-linecap="round">
        <rect x="5" y="6" width="20" height="20" rx="2"/>
        <path d="M5 11h20M9 4v4M13 4v4M17 4v4M21 4v4"/>
        <path d="M9 15h2M13 15h2M17 15h2M9 19h2M13 19h2M9 23h2"/>
        <circle cx="23" cy="23" r="5" fill="#1d4690"/>
        <path d="M23 20.5v2.7l1.8 1.2"/>
      </g>
    </symbol>
  </defs>
</svg>

<section class="ad ad--post" aria-label="Square post ad">
  <div class="ad__scenery" role="img" aria-label="Aerial photo of misty Alaskan tundra with snowy cliffs and a waterfall under a pale sky, fading into deep blue"></div>

  <div class="brand"><span class="brand__dot"></span>Skyreach Broadband</div>

  <h1 class="headline">
    <span class="headline__line headline__line--1">Introduce our new <span class="headline__big">Z</span><span class="headline__caps">ENIRO</span></span>
    <span class="headline__line headline__line--2">Internet service</span>
  </h1>

  <div class="panel panel--features">
    <ul class="features">
      <li style="top:31px">Speeds to 500 mpbs</li>
      <li style="top:65px">Packages start at only $89.99<br>for speeds to 100mbps</li>
      <li style="top:126px">Fiber Optic based connection,<br>not satellite</li>
      <li style="top:184px">Extreme low latency,<br>consistent speeds</li>
    </ul>
  </div>

  <div class="panel panel--perks">
    <div class="free-tag">FREE</div>
    <div class="perk" style="top:45px"><svg width="26" height="26"><use href="#icon-equipment"/></svg>Equipment</div>
    <div class="perk" style="top:96px"><svg width="26" height="26"><use href="#icon-install"/></svg>Installation</div>
    <div class="perk" style="top:147px"><svg width="26" height="26"><use href="#icon-router"/></svg>Wifi Router</div>
    <div class="perk" style="top:194px"><svg width="26" height="26"><use href="#icon-calendar"/></svg>1st Month of<br>Service</div>
  </div>

  <div class="url-bar">
    <span class="url-bar__dot" style="left:21px"></span>
    More information <strong>www.skyreachlink.com</strong>
    <span class="url-bar__dot" style="left:521px"></span>
  </div>
</section>

<section class="ad ad--story" aria-label="Vertical story ad">
  <div class="ad__scenery" role="img" aria-label="Aerial photo of misty Alaskan tundra with snowy cliffs and a waterfall under a pale sky, fading into deep blue"></div>

  <div class="brand"><span class="brand__dot"></span>Skyreach Broadband</div>

  <h1 class="headline">
    <span class="headline__line headline__line--1">Introduce our new <span class="headline__big">Z</span><span class="headline__caps">ENIRO</span></span>
    <span class="headline__line headline__line--2">Internet service</span>
  </h1>

  <div class="panel panel--features">
    <ul class="features">
      <li style="top:28px">Speeds to 500 mpbs</li>
      <li style="top:59px">Packages start at only $89.99<br>for speeds to 100mbps</li>
      <li style="top:114px">Fiber Optic based connection,<br>not satellite</li>
      <li style="top:167px">Extreme low latency,<br>consistent speeds</li>
    </ul>
  </div>

  <div class="panel panel--perks"></div>
  <div class="free-tag">FREE</div>
  <div class="perk" style="left:126px"><svg width="32" height="32"><use href="#icon-equipment"/></svg>Equipment</div>
  <div class="perk" style="left:205px"><svg width="32" height="32"><use href="#icon-install"/></svg>Installation</div>
  <div class="perk" style="left:285px"><svg width="32" height="32"><use href="#icon-router"/></svg>Wifi Router</div>
  <div class="perk" style="left:370px"><svg width="32" height="32"><use href="#icon-calendar"/></svg>1st Month of<br>Service</div>

  <div class="url-bar">
    <span class="url-bar__dot" style="left:14px"></span>
    More information <strong>www.skyreachlink.com</strong>
    <span class="url-bar__dot" style="left:374px"></span>
  </div>
</section>

<p class="caption" style="left:344px;top:820px">Post optimized | 1:1 | 1080x1080px</p>
<p class="caption" style="left:926px;top:921px">Story optimized | 9:16 | 1080x1920px</p>

</body>
</html>
```